Flooring & Interior Design showroom

Just bought this business- Maple Terrace Flooring & Interiors. Love our logo (we are on Maple Terrace )and colors
Forest green, gold and black
Love that the back lists everything we do. We no longer have stonavelle but need to add in LVP/ SPC and need to take out tirelli shadehouse logo at the bottom and use the zumo logo instead (maybe? open to suggestions)

Not in love with our cards- I want a higher end look
I hate the gradient poop color we have now.
Would love if they were all black - maybe or ??
or had a foil or embossing?

```html
<!DOCTYPE html>
<html lang="en">
<head>
<meta charset="utf-8">
<title>Maple Terrace Flooring &amp; Interiors — Business Card</title>
<link rel="stylesheet" href="https://fonts.googleapis.com/css2?family=Montserrat:wght@400;600;700&family=Barlow:wght@400&display=swap">
<style>
  :root {
    --page: #ffffff;
    --card-dark: #050505;
    --card-light: #1e1e1e;
    --ink: #ffffff;
  }
  * { box-sizing: border-box; margin: 0; padding: 0; }
  html, body {
    width: 1076px; height: 1200px; overflow: hidden;
    background: var(--page);
  }
  body { position: relative; font-family: "Montserrat", sans-serif; color: var(--ink); }

  .card {
    position: absolute; left: 70px; width: 941px; height: 524px;
    background: linear-gradient(45deg, var(--card-dark) 0%, #0e0e0e 55%, var(--card-light) 100%);
  }
  .card--front { top: 43px; }
  .card--back  { top: 639px; }

  /* business name set as text */
  .brand {
    position: absolute; text-align: center;
    font-family: "Montserrat", sans-serif; font-weight: 600; color: var(--ink);
    line-height: 1.15;
  }
  .brand .line-main { display: block; font-size: 34px; letter-spacing: 0.08em; padding-left: 0.08em; }
  .brand .line-sub  { display: block; font-size: 13px; letter-spacing: 0.3em; padding-left: 0.3em; margin-top: 10px; }

  .card--front .brand { left: 0; right: 0; top: 122px; }

  .license {
    position: absolute; top: 14px; right: 23px;
    font-size: 17px; font-weight: 400; letter-spacing: 0.01em;
  }
  .person__name {
    position: absolute; left: 0; right: 0; top: 285px; text-align: center;
    font-size: 55px; font-weight: 700; letter-spacing: -0.01em; line-height: 1;
  }
  .person__title {
    position: absolute; left: 0; right: 0; top: 343px; text-align: center;
    font-size: 17px; font-weight: 400; letter-spacing: 0.32em; padding-left: 0.32em;
  }
  .person__email {
    position: absolute; left: 0; right: 0; top: 386px; text-align: center;
    font-size: 18px; font-weight: 400; letter-spacing: 0.3em; padding-left: 0.3em;
  }
  .contacts {
    position: absolute; left: 0; right: 0; top: 443px;
    display: flex; justify-content: center; gap: 36px;
    font-size: 17px; letter-spacing: 0.24em;
  }
  .contacts b { font-weight: 700; margin-right: 6px; }
  .address {
    position: absolute; left: 0; right: 0; top: 474px; text-align: center;
    font-size: 17px; letter-spacing: 0.26em; padding-left: 0.26em;
  }

  /* back */
  .card--back .brand { left: 40px; width: 320px; top: 104px; }
  .card--back .brand .line-main { font-size: 28px; letter-spacing: 0.06em; }
  .card--back .brand .line-sub { font-size: 11px; letter-spacing: 0.26em; }

  .partner {
    position: absolute; left: 63px; width: 220px; top: 276px;
    display: flex; flex-direction: column; align-items: center; gap: 10px;
  }
  .partner__mark { width: 36px; height: 36px; border-radius: 50%; background: var(--ink); }
  .partner__name { font-size: 24px; font-weight: 700; letter-spacing: -0.01em; }

  .review {
    position: absolute; left: 80px; width: 186px; top: 414px;
    display: flex; align-items: center; justify-content: center; gap: 12px;
  }
  .review__name { font-size: 46px; font-weight: 700; line-height: 1; }
  .review__mark { width: 30px; height: 30px; border-radius: 50%; background: var(--ink); }

  .services {
    position: absolute; top: 58px; list-style: none;
    font-family: "Barlow", sans-serif; font-size: 26px; font-weight: 400;
  }
  .services--a { left: 403px; }
  .services--b { left: 623px; }
  .services li {
    position: relative; height: 37.4px; line-height: 37.4px; padding-left: 30px;
  }
  .services li::before {
    content: ""; position: absolute; left: 2px; top: 14px;
    width: 8px; height: 8px; background: var(--ink); transform: rotate(45deg);
  }
  .hotline {
    position: absolute; left: 390px; top: 412px;
    font-size: 65px; font-weight: 700; letter-spacing: 0.01em; line-height: 1;
  }
  .website {
    position: absolute; left: 392px; top: 474px;
    font-size: 25px; font-weight: 600; letter-spacing: 0.12em;
  }
</style>
</head>
<body>

<section class="card card--front">
  <p class="license">CA LIC # 418062</p>
  <p class="brand"><span class="line-main">MAPLE TERRACE</span><span class="line-sub">FLOORING &amp; INTERIORS</span></p>
  <h1 class="person__name">NORA WELLAND</h1>
  <p class="person__title">OWNER/ DESIGNER</p>
  <p class="person__email">NORA@MAPLETERRACEFLOORING.COM</p>
  <p class="contacts">
    <span><b>STORE</b> 831.555.0184</span>
    <span><b>CELL</b> 559-555-0137</span>
    <span><b>FAX</b> 831.555.0162</span>
  </p>
  <p class="address">726 MAPLE TERRACE, CYPRESS BAY CA 93999</p>
</section>

<section class="card card--back">
  <p class="brand"><span class="line-main">MAPLE TERRACE</span><span class="line-sub">FLOORING &amp; INTERIORS</span></p>

  <div class="partner">
    <span class="partner__mark"></span>
    <span class="partner__name">Lindqvist Shades</span>
  </div>

  <div class="review">
    <span class="review__name">zumo</span>
    <span class="review__mark"></span>
  </div>

  <ul class="services services--a">
    <li>AREA RUGS</li>
    <li>BLINDS</li>
    <li>CARPET</li>
    <li>CORK</li>
    <li>HARDWOOD</li>
    <li>LAMINATE</li>
    <li>SHEERS</li>
    <li>VALANCES</li>
    <li>VINYL</li>
  </ul>
  <ul class="services services--b">
    <li>BED SPREADS</li>
    <li>DRAPERIES</li>
    <li>LVP/ SPC</li>
    <li>FABRIC</li>
    <li>MOTORIZED SHADES</li>
    <li>PILLOWS</li>
    <li>SHUTTERS</li>
    <li>UPHOLSTERY</li>
    <li>VERTICALS</li>
  </ul>

  <p class="hotline">831.555.0184</p>
  <p class="website">www.mapleterraceflooring.com</p>
</section>

</body>
</html>
```